Family Owned Construction Company Needs Modern Business Cards

We need a new design for our business cards. We are a family owned construction company, Brantwell Construction, based in Mendon, Vermont and would like to add in our new logo and find a more modern look. We also want to use our old to make sure people know who we are. We do site development, highway, environmental, demolition, utility and aggregate.

Contact Information for Business Card

We want to have the office address, 418 Quarry Ridge Road, Alder Falls, NH 03299 and our phone (802) 555-0137 and fax (802) 555-0164 on there as well. Our website is www.brantwellinc.example. There should be a place for the person's name, title, cell number, and email address on the card. Words that we would like to be associated with our company are honesty, predictable, reliable, integrity, dedicated, built right quality, consistent, whatever it takes, and innovation. Safety is also very important to us.

Font styles to use
Serif
Sans Serif
Other font styles liked:
• Square 721 Extented

Colors
0255a3
ffffff

Requirements
Must have
• Office address, phone number and fax number. New logo with excavator
Nice to have
• That we do site development, highway, environmental, demolition, utility, and aggregate. Both logos

```html
<!DOCTYPE html>
<html lang="en">
<head>
<meta charset="utf-8">
<title>Brantwell Construction – Business Cards</title>
<link rel="stylesheet" href="https://fonts.googleapis.com/css2?family=Arimo:wght@400;700&family=Tinos:wght@700&display=swap">
<style>
  :root {
    --brand-blue: #0d3279;
    --brand-blue-light: #0a3f8c;
    --brand-blue-dark: #0b2766;
    --paper: #ffffff;
    --backdrop: #e3e4e6;
    --ink-grey: #4a4f58;
  }
  * { box-sizing: border-box; margin: 0; padding: 0; }
  html, body { width: 1200px; height: 1200px; overflow: hidden; }
  body {
    background: var(--backdrop);
    font-family: "Arimo", Arial, sans-serif;
    position: relative;
  }
  .card {
    position: absolute;
    left: 150px;
    width: 900px;
    height: 514px;
    overflow: hidden;
    box-shadow: 0 6px 18px rgba(0,0,0,0.12);
  }

  /* Front side */
  .card--front { top: 66px; background: var(--paper); }
  .wordmark {
    position: absolute;
    font-family: "Arimo", Arial, sans-serif;
    font-weight: 700;
    text-transform: uppercase;
    letter-spacing: 1px;
    line-height: 1.05;
  }
  .card--front .wordmark {
    left: 360px; top: 92px;
    color: var(--brand-blue);
    font-size: 40px;
  }
  .holder {
    position: absolute;
    left: 360px; top: 200px;
    color: var(--brand-blue);
  }
  .holder__name {
    font-family: "Tinos", "Times New Roman", serif;
    font-weight: 700;
    font-size: 26px;
    text-transform: uppercase;
  }
  .holder__sep { color: var(--brand-blue); font-weight: 400; margin: 0 6px; font-size: 26px; }
  .holder__title { font-size: 22px; color: var(--ink-grey); }
  .holder__cell {
    display: flex; align-items: center; gap: 8px;
    margin-top: 8px; font-size: 20px; color: var(--ink-grey);
  }
  .rule {
    position: absolute; left: 0; width: 100%; height: 3px;
    background: var(--brand-blue);
  }
  .rule--top { top: 282px; }
  .rule--bottom { top: 436px; }
  .contact-band {
    position: absolute; left: 0; top: 298px;
    width: 100%; height: 124px;
    background: var(--brand-blue);
    color: var(--paper);
    display: flex; align-items: center;
  }
  .contact-band__col {
    display: flex; flex-direction: column; gap: 14px;
    font-size: 21px; letter-spacing: 0.5px;
  }
  .contact-band__col--office { width: 470px; align-items: flex-end; padding-right: 22px; }
  .contact-band__col--web { padding-left: 22px; align-items: flex-start; }
  .contact-band__divider { width: 2px; height: 84px; background: rgba(255,255,255,0.7); }
  .contact-line { display: flex; align-items: center; gap: 10px; white-space: nowrap; }
  .contact-band__col--web .contact-line { letter-spacing: 2px; }

  /* Back side */
  .card--back {
    top: 620px;
    background: linear-gradient(135deg, var(--brand-blue-dark) 0%, var(--brand-blue) 50%, var(--brand-blue-light) 100%);
    color: var(--paper);
  }
  .card--back .wordmark {
    left: 170px; top: 170px;
    color: var(--paper);
    font-size: 48px;
  }
  .address {
    position: absolute; left: 170px; top: 300px;
    font-size: 24px; letter-spacing: 0.5px;
    white-space: nowrap;
  }
  svg.icon { width: 20px; height: 20px; flex: none; }
</style>
</head>
<body>

  <section class="card card--front" aria-label="Business card front">
    <div class="wordmark">Brantwell<br>Construction</div>

    <div class="holder">
      <div>
        <span class="holder__name">Jordan Hale</span><span class="holder__sep">|</span><span class="holder__title">Director</span>
      </div>
      <div class="holder__cell">
        <svg class="icon" viewBox="0 0 20 20" aria-hidden="true"><rect x="5" y="1.5" width="10" height="17" rx="2" fill="none" stroke="#4a4f58" stroke-width="1.8"/><circle cx="10" cy="15" r="1.2" fill="#4a4f58"/></svg>
        1-603-555-0199
      </div>
    </div>

    <div class="rule rule--top"></div>
    <div class="contact-band">
      <div class="contact-band__col contact-band__col--office">
        <div class="contact-line">(802) 555-0137
          <svg class="icon" viewBox="0 0 20 20" aria-hidden="true"><rect x="1" y="1" width="18" height="18" rx="3" fill="#fff"/><path d="M6.5 4.5l2 2-1.2 1.6c.8 1.7 2 2.9 3.6 3.6l1.6-1.2 2 2-1.3 2c-4.5-.4-8.2-4.1-8.6-8.6z" fill="#0d3279"/></svg>
        </div>
        <div class="contact-line">jordan@brantwellconstruction.example
          <svg class="icon" viewBox="0 0 20 20" aria-hidden="true"><rect x="1" y="1" width="18" height="18" rx="3" fill="#fff"/><rect x="4" y="6" width="12" height="8" fill="none" stroke="#0d3279" stroke-width="1.5"/><path d="M4 6l6 4.5L16 6" fill="none" stroke="#0d3279" stroke-width="1.5"/></svg>
        </div>
      </div>
      <div class="contact-band__divider"></div>
      <div class="contact-band__col contact-band__col--web">
        <div class="contact-line">
          <svg class="icon" viewBox="0 0 20 20" aria-hidden="true"><rect x="1" y="1" width="18" height="18" rx="3" fill="#fff"/><rect x="4.5" y="8" width="11" height="7" fill="#0d3279"/><rect x="6.5" y="4.5" width="7" height="4" fill="none" stroke="#0d3279" stroke-width="1.4"/></svg>
          (802) 555-0164
        </div>
        <div class="contact-line">
          <svg class="icon" viewBox="0 0 20 20" aria-hidden="true"><circle cx="10" cy="10" r="9" fill="#fff"/><circle cx="10" cy="10" r="6" fill="none" stroke="#0d3279" stroke-width="1.3"/><ellipse cx="10" cy="10" rx="2.6" ry="6" fill="none" stroke="#0d3279" stroke-width="1.2"/><path d="M4 10h12" stroke="#0d3279" stroke-width="1.2"/></svg>
          brantwellinc.example
        </div>
      </div>
    </div>
    <div class="rule rule--bottom"></div>
  </section>

  <section class="card card--back" aria-label="Business card back">
    <div class="wordmark">Brantwell<br>Construction</div>
    <p class="address">418 Quarry Ridge Road, Alder Falls, NH 03299</p>
  </section>

</body>
</html>
```